Hallowmere Business Card

This is the personal business card for Dr Glen Hallowmere and convers three area of his professional activity - all of them involve (foreign) languages:
o RQVB International Ltd - A translation company with 50 staff. Trades internationally
o TideLatch Ltd - a global online auction marketplace for translation services (startup)
o Vowelcraft - cutting edge technology from the brain sciences which helps learners assimilate the sound patterns of a new language (startup)

Target Market(s)

The card needs to have a "cutting edge" feel - but for a fairly conservative audience - academics, investors.

Industry/Entity Type

Business

Requirements
Must have
• Text:
Dr Glen Hallowmere

Co-founder RQVB International Ltd (Language translation)
Founder TideLatch Ltd (Translation marketplace)
Founder Vowelcraft (Language acquisition)

email: glen.morrow@lintmail.example
Phone: +64 21 555 3916
Twitter: @GlenMorrow4

```html
<!DOCTYPE html>
<html lang="en">
<head>
<meta charset="utf-8">
<title>Hallowmere Business Card</title>
<link rel="stylesheet" href="https://fonts.googleapis.com/css2?family=Arimo:wght@400;700&display=swap">
<style>
  :root {
    --navy: #0c3466;
    --paper: #ffffff;
    --accent: #5b9fd9;
  }
  html, body {
    margin: 0;
    padding: 0;
    width: 1200px;
    height: 359px;
    overflow: hidden;
    background: var(--paper);
    font-family: "Arimo", Arial, sans-serif;
  }
  .sheet {
    position: relative;
    width: 1200px;
    height: 359px;
  }
  .card {
    position: absolute;
    top: 0;
    width: 577px;
    height: 344px;
    background: var(--navy);
    overflow: hidden;
  }
  .card--front { left: 0; }
  .card--back { left: 623px; }

  .front-block {
    position: absolute;
    left: 0;
    top: 91px;
    width: 177px;
    height: 190px;
    background: var(--paper);
  }
  .front-name {
    position: absolute;
    left: 20px;
    top: 241px;
    margin: 0;
    font-size: 9.5px;
    font-weight: 700;
    letter-spacing: -0.1px;
    color: var(--navy);
    white-space: nowrap;
  }

  .back-name {
    position: absolute;
    left: 73px;
    top: 104px;
    margin: 0;
    font-size: 31px;
    font-weight: 700;
    letter-spacing: -0.3px;
    line-height: 1;
    color: var(--paper);
    white-space: nowrap;
  }
  .roles {
    position: absolute;
    left: 73px;
    top: 138px;
    margin: 0;
    padding: 0;
    list-style: none;
    font-size: 14px;
    line-height: 17.5px;
    color: var(--accent);
    white-space: nowrap;
  }
  .contact {
    position: absolute;
    left: 73px;
    top: 191px;
    margin: 0;
    font-size: 14px;
    line-height: 17.5px;
    color: var(--paper);
    white-space: nowrap;
    font-style: normal;
  }
  .contact p { margin: 0; }
</style>
</head>
<body>
<main class="sheet">
  <section class="card card--front" aria-label="Card front">
    <div class="front-block">
    </div>
    <p class="front-name">DR GLEN HALLOWMERE</p>
  </section>

  <section class="card card--back" aria-label="Card back">
    <h1 class="back-name">DR GLEN HALLOWMERE</h1>
    <ul class="roles">
      <li>Co-founder RQVB International Ltd (Language translation)</li>
      <li>Founder TideLatch Ltd (Translation marketplace)</li>
      <li>Founder Vowelcraft (Language acquisition)</li>
    </ul>
    <address class="contact">
      <p>email: glen.morrow@lintmail.example Phone: +64 21 555 3916</p>
      <p>Twitter: @GlenMorrow4</p>
    </address>
  </section>
</main>
</body>
</html>
```